Conservative, Modern and Sharp Builder Business card

Hi there,
We would like to update our existing business card.
I have attached photos of existing business card, logo and van sign.

I would like the business card to also list what we do :
Renovation • New Build • Alteration
Extension • Bathroom • Maintenance.(Seperated by dots)

Contact number : 021 0483 0752
(With that exact spacing)

Ideally when people looking from about 2-3 metres, they know that it is a builder’s business card

Open to suggestions on fonts, layout, style of business card

PLEASE ONLY SUBMIT YOUR BEST OR MAX 3 DESIGNS FOR EACH DESIGNER

Thanks

Industry/Entity Type

Construction. Renovation

Contact Information for Business Card

Details should be the same as the existing card. And addition of what we do.

Requirements
Should not have
• The new business card must not have the same layout as our existing one. Thanks

```html
<!DOCTYPE html>
<html lang="en">
<head>
<meta charset="utf-8">
<title>KeelBuild Business Card</title>
<link href="https://fonts.googleapis.com/css2?family=Poppins:wght@400;600;700&display=swap" rel="stylesheet">
<style>
  :root {
    --stage: #2b2b2b;
    --card: #1f1f20;
    --card-back: #0d0d0e;
    --ink: #ffffff;
    --ink-soft: #d9d9d9;
    --rule: #6a6a6a;
  }
  * { box-sizing: border-box; margin: 0; padding: 0; }
  html, body { width: 1200px; height: 1108px; overflow: hidden; }
  body {
    background: var(--stage);
    font-family: "Poppins", sans-serif;
    color: var(--ink);
    display: flex;
    align-items: center;
    justify-content: center;
    gap: 80px;
  }
  .card {
    width: 440px;
    height: 680px;
    border-radius: 26px;
    position: relative;
    overflow: hidden;
  }
  .card--front {
    background: var(--card);
    display: flex;
    flex-direction: column;
    align-items: center;
    padding-top: 110px;
    text-align: center;
  }
  .brand {
    display: flex;
    align-items: center;
    gap: 14px;
  }
  .brand__square {
    width: 22px; height: 22px;
    background: var(--ink);
  }
  .brand__name {
    font-weight: 700;
    font-size: 58px;
    letter-spacing: -1px;
    line-height: 1;
  }
  .person { margin-top: 92px; }
  .person__name { font-weight: 600; font-size: 27px; }
  .person__role { font-size: 19px; color: var(--ink-soft); margin-top: -2px; }
  .contact-rule {
    display: flex; align-items: center; gap: 12px;
    width: 300px; margin-top: 18px;
  }
  .contact-rule::before, .contact-rule::after {
    content: ""; flex: 1; height: 1px; background: var(--rule);
  }
  .icons { display: flex; gap: 6px; }
  .icon {
    width: 38px; height: 38px; border-radius: 8px;
    background: var(--ink);
    display: flex; align-items: center; justify-content: center;
  }
  .contact { margin-top: 14px; line-height: 1.3; }
  .contact__phone { font-weight: 600; font-size: 26px; letter-spacing: 1px; }
  .contact__line { font-size: 21px; }
  .divider { width: 300px; height: 1px; background: var(--rule); margin-top: 22px; }
  .social {
    display: flex; align-items: center; gap: 12px;
    margin-top: 22px; font-size: 22px;
  }
  .social__mark {
    width: 26px; height: 26px; border-radius: 50%;
    border: 2px solid var(--ink);
  }
  .card--back { background: var(--card-back); }
  .pattern {
    position: absolute; inset: 0;
    background: linear-gradient(225deg, #5a5a5c 0%, #2a2a2c 40%, #0b0b0c 75%);
  }
  .back-brand {
    position: absolute; right: 60px; top: 430px;
    display: flex; align-items: center; gap: 10px;
  }
  .back-brand__square { width: 12px; height: 12px; background: var(--ink); }
  .back-brand__name { font-weight: 700; font-size: 30px; }
  .services {
    position: absolute; left: 0; right: 0; bottom: 70px;
    text-align: center; font-size: 19px; line-height: 1.45;
  }
</style>
</head>
<body>
  <section class="card card--front">
    <div class="brand">
      <span class="brand__square"></span>
      <span class="brand__name">KeelBuild</span>
    </div>
    <div class="person">
      <p class="person__name">Tomas Verrill</p>
      <p class="person__role">Residential Builder</p>
    </div>
    <div class="contact-rule">
      <div class="icons">
        <span class="icon">
          <svg width="22" height="22" viewBox="0 0 24 24"><path fill="#1f1f20" d="M6.6 10.8a15.1 15.1 0 0 0 6.6 6.6l2.2-2.2c.3-.3.7-.4 1-.2 1.1.4 2.3.6 3.6.6.6 0 1 .4 1 1V20c0 .6-.4 1-1 1A17 17 0 0 1 3 4c0-.6.4-1 1-1h3.5c.6 0 1 .4 1 1 0 1.3.2 2.5.6 3.6.1.3 0 .7-.2 1z"/></svg>
        </span>
        <span class="icon">
          <svg width="22" height="22" viewBox="0 0 24 24"><rect x="3" y="5" width="18" height="14" rx="1" fill="none" stroke="#1f1f20" stroke-width="2"/><path d="M3 6l9 7 9-7" fill="none" stroke="#1f1f20" stroke-width="2"/></svg>
        </span>
        <span class="icon">
          <svg width="22" height="22" viewBox="0 0 24 24"><circle cx="12" cy="12" r="9" fill="none" stroke="#1f1f20" stroke-width="2"/><path d="M3 12h18M12 3c3 3 3 15 0 18M12 3c-3 3-3 15 0 18" fill="none" stroke="#1f1f20" stroke-width="1.6"/></svg>
        </span>
      </div>
    </div>
    <div class="contact">
      <p class="contact__phone">021 0483 0752</p>
      <p class="contact__line">KeelBuild@Mailhub.nz</p>
      <p class="contact__line">www.KeelBuild.nz</p>
    </div>
    <div class="divider"></div>
    <div class="social">
      <span class="social__mark"></span>
      <span>KeelBuild.nz</span>
    </div>
  </section>

  <section class="card card--back">
    <div class="pattern" role="img" aria-label="Glossy repeating brand monogram pattern across the card"></div>
    <div class="back-brand">
      <span class="back-brand__square"></span>
      <span class="back-brand__name">KeelBuild</span>
    </div>
    <p class="services">Renovation • New Build • Alteration<br>Extension • Bathroom • Maintenance</p>
  </section>
</body>
</html>
```